velmo tarsik

WANTING A DL FLYER DESIGN
Wanting a design to advertise the supply and install of my new VELMO QT TARSIK in dash GPS system.
Wanting pictures on it wilth colours.
This product is going to be sold in NEW CAR dealerships.

My company is all about installing in dash GPS touch screens. made to fit into your dash.

Must state on the flyer:
$995 fitted - Please make the price bold so it stands out
Steering wheel controls still work
DVD/VCD/MP3/SD/USB/melqo/CD/RDS Radio/GPS plus heaps more.
Fits ZB, ZBN ZBW & Moonbrisk
Built into the dash, made to fit!

New car customers

Wheel

• Please incorporate my logo into the flyer. will be uploading later today
My email - tomparvey@mailquist.net
My Phone - 0412 568 214
• wanting the main idea to be based on the stereo picture.

```html
<!DOCTYPE html>
<html lang="en">
<head>
<meta charset="utf-8">
<title>Velmo QT Tarsik In-Dash GPS – $995 Fitted</title>
<link rel="stylesheet" href="https://fonts.googleapis.com/css2?family=Josefin+Sans:wght@300;400;500;600&display=swap">
<style>
  :root {
    --navy: #2c3f73;
    --white: #ffffff;
    --stereo-black: #17181b;
    --stereo-dark: #3a3c41;
    --stereo-silver: #a4a6aa;
    --stereo-grey: #6e7075;
    --screen-deep: #1d3f9a;
    --screen-blue: #3b6fd0;
  }
  * { margin: 0; padding: 0; box-sizing: border-box; }
  html, body {
    width: 1200px;
    height: 543px;
    overflow: hidden;
    background: var(--navy);
  }
  .flyer {
    position: relative;
    width: 1200px;
    height: 543px;
    background: var(--navy);
    color: var(--white);
    font-family: "Josefin Sans", sans-serif;
  }
  .product-photo {
    position: absolute;
    left: 0;
    top: 0;
    width: 474px;
    height: 543px;
    background:
      radial-gradient(ellipse 46% 22% at 48% 29%, var(--screen-blue) 0%, var(--screen-deep) 55%, rgba(29,63,154,0) 100%),
      linear-gradient(180deg,
        var(--stereo-black) 0%,
        var(--stereo-dark) 8%,
        var(--stereo-grey) 50%,
        var(--stereo-silver) 60%,
        var(--stereo-grey) 74%,
        var(--stereo-dark) 88%,
        var(--stereo-black) 100%);
  }
  .price {
    position: absolute;
    left: 528px;
    top: 8px;
    display: flex;
    align-items: baseline;
    white-space: nowrap;
  }
  .price-amount {
    font-weight: 500;
    font-size: 218px;
    line-height: 1;
    letter-spacing: -10px;
  }
  .price-label {
    font-weight: 300;
    font-size: 52px;
    letter-spacing: 1px;
    margin-left: 18px;
  }
  .features {
    position: absolute;
    left: 534px;
    top: 210px;
    list-style: none;
    font-weight: 400;
    font-size: 24px;
    line-height: 34px;
    letter-spacing: 0.4px;
  }
  .brand {
    position: absolute;
    left: 474px;
    right: 0;
    top: 422px;
    display: flex;
    justify-content: center;
    align-items: center;
    gap: 12px;
  }
  .brand-mark {
    width: 46px;
    height: 46px;
    background: var(--white);
  }
  .brand-name {
    font-weight: 600;
    font-size: 32px;
    color: var(--white);
  }
  .contact {
    position: absolute;
    left: 474px;
    right: 0;
    top: 492px;
    text-align: center;
    font-weight: 300;
    font-size: 19px;
    letter-spacing: 0.5px;
  }
  .contact .divider { margin: 0 18px; }
</style>
</head>
<body>
  <main class="flyer">
    <div class="product-photo" role="img" aria-label="Photo of the Velmo QT Tarsik in-dash touch screen stereo fitted in the dashboard, showing its menu screen and control buttons"></div>

    <div class="price">
      <span class="price-amount">$995</span>
      <span class="price-label">FITTED</span>
    </div>

    <ul class="features">
      <li>Built into the dash, made to fit!</li>
      <li>Steering wheel controls still work</li>
      <li>DVD/VCD/MP3/SD/USB/melqo/CD/RDS Radio/GPS</li>
      <li>plus heaps more.</li>
      <li>Fits ZB, ZBN ZBW &amp; Moonbrisk</li>
    </ul>

    <div class="brand">
      <span class="brand-mark" aria-hidden="true"></span>
      <span class="brand-name">Orvane Creations</span>
    </div>

    <p class="contact">
      <span class="email">tomparvey@mailquist.net</span><span class="divider">|</span><span class="phone">0412 568 214</span>
    </p>
  </main>
</body>
</html>
```